Business Card Design For DJ Company

I'm rebranding my wedding and event dj company. I am looking for a modern, luxury, & fun design to match my new logo and website design. Please see attached logo and new webpage design. Colors should match. Design should flow with logo and website for recognition. I want to attract young adults. I plan on printing metallic finish cards so please keep hat in mind.

Target Market(s)

Millennials

Contact Information for Business Card

Name: Dario Colvento
Company: Cedar Hollow Mix DJ
Services: DJ – Photo Booth – Event Lighting – LED Robot

Website: www.cedarhollowmixdj.example
Email: dario@cedarhollowmixdj.example
Phone: (555)417-9382

Instagram: @chmixdj
Facebook: @chmixdj
Twitter - @chmixdj

Se Habla Español

Font styles to use
Serif
Sans Serif

Colors

Designer to choose colors to be used in the design.

Requirements
Nice to have
• Transparent Gradient background - Image related to weddings

```html
<!DOCTYPE html>
<html lang="en">
<head>
<meta charset="utf-8">
<title>Cedar Hollow Mix DJ — Business Card</title>
<link href="https://fonts.googleapis.com/css2?family=Roboto+Condensed:wght@300;400;700&display=swap" rel="stylesheet">
<style>
  :root {
    --bg: #e4e5e8;
    --paper: #ffffff;
    --green: #62c232;
    --green-light: #94e04c;
    --green-dark: #3fae2e;
    --orange: #f47d12;
    --blue: #22a7e0;
    --white: #ffffff;
  }
  * { box-sizing: border-box; margin: 0; padding: 0; }
  html, body { width: 1200px; height: 800px; overflow: hidden; }
  body {
    background: var(--bg);
    font-family: "Roboto Condensed", Arial, sans-serif;
    position: relative;
  }
  .card {
    position: absolute;
    top: 245px;
    width: 540px;
    height: 309px;
    background: var(--paper);
    overflow: hidden;
    box-shadow: 0 6px 18px rgba(0,0,0,0.12);
  }
  .card--back { left: 40px; }
  .card--front { left: 620px; }

  /* brand mark */
  .brand {
    position: absolute;
    display: flex;
    flex-direction: column;
    align-items: center;
    gap: 10px;
  }
  .brand__dot {
    width: 64px; height: 64px;
    border: 5px solid var(--blue);
    border-radius: 50%;
  }
  .brand__name {
    font-weight: 700;
    font-size: 21px;
    color: var(--orange);
    text-align: center;
    line-height: 1.1;
    letter-spacing: 0.5px;
    text-transform: uppercase;
  }

  /* back side */
  .card--back .accent-bar {
    position: absolute;
    left: 0; top: 24px;
    width: 9px; height: 96px;
    background: var(--green);
  }
  .card--back .brand { left: 26px; top: 60px; width: 180px; }
  .contact-panel {
    position: absolute;
    left: 222px; top: 58px;
    right: 0; bottom: 0;
    background: linear-gradient(135deg, var(--green-light) 0%, var(--green) 55%, var(--green-dark) 100%);
    border-top-left-radius: 26px;
    padding: 22px 22px 0 26px;
    color: var(--white);
  }
  .contact-panel__name {
    font-weight: 300;
    font-size: 30px;
    padding-bottom: 8px;
    border-bottom: 1.5px dashed rgba(255,255,255,0.85);
    margin-bottom: 12px;
  }
  .contact-list { list-style: none; }
  .contact-list li {
    display: flex;
    align-items: center;
    gap: 9px;
    font-weight: 300;
    font-size: 15.5px;
    line-height: 24px;
  }
  .contact-list .icon {
    width: 15px; height: 15px;
    border-radius: 50%;
    background: var(--orange);
    flex: none;
    display: flex; align-items: center; justify-content: center;
  }
  .contact-list .icon svg { width: 9px; height: 9px; }

  /* front side */
  .card--front .brand { left: 0; right: 0; top: 38px; }
  .service-tab {
    position: absolute;
    left: 0; top: 186px;
    width: 110px; height: 60px;
    background: var(--orange);
    border-top-right-radius: 22px;
  }
  .service-band {
    position: absolute;
    left: 62px; right: 0; top: 200px; bottom: 0;
    background: linear-gradient(90deg, var(--green) 0%, var(--green-light) 100%);
    border-top-left-radius: 26px;
    display: flex;
    align-items: center;
    padding-left: 30px;
    gap: 18px;
    color: var(--white);
  }
  .service-band span {
    font-weight: 300;
    font-size: 21px;
  }
  .service-band span::before {
    content: "•";
    margin-right: 6px;
  }
</style>
</head>
<body>

  <section class="card card--back" aria-label="Business card back">
    <div class="accent-bar"></div>
    <div class="brand">
      <div class="brand__dot"></div>
      <div class="brand__name">Cedar Hollow<br>Mix DJ</div>
    </div>
    <div class="contact-panel">
      <h1 class="contact-panel__name">Dario Colvento</h1>
      <ul class="contact-list">
        <li><span class="icon"><svg viewBox="0 0 10 10"><circle cx="5" cy="5" r="4" fill="none" stroke="#fff" stroke-width="1.2"/><path d="M1 5h8M5 1c-2 2.5-2 5.5 0 8M5 1c2 2.5 2 5.5 0 8" fill="none" stroke="#fff" stroke-width="1"/></svg></span>www.cedarhollowmixdj.example</li>
        <li><span class="icon"><svg viewBox="0 0 10 10"><rect x="1" y="2" width="8" height="6" fill="none" stroke="#fff" stroke-width="1.2"/><path d="M1 2l4 3.5L9 2" fill="none" stroke="#fff" stroke-width="1.1"/></svg></span>dario@cedarhollowmixdj.example</li>
        <li><span class="icon"><svg viewBox="0 0 10 10"><path d="M2 1l2 2-1 1.3c.7 1.3 1.4 2 2.7 2.7L7 6l2 2-1.4 1.4C4.5 9 1 5.5.6 2.4z" fill="#fff"/></svg></span>(555)417-9382</li>
        <li><span class="icon"></span>@chmixdj</li>
        <li><span class="icon"></span>social.example/chmixdj</li>
        <li><span class="icon"></span>@chmixdj</li>
      </ul>
    </div>
  </section>

  <section class="card card--front" aria-label="Business card front">
    <div class="brand">
      <div class="brand__dot"></div>
      <div class="brand__name">Cedar Hollow Mix DJ</div>
    </div>
    <div class="service-tab"></div>
    <div class="service-band">
      <span>DJ</span>
      <span>Photo Booth</span>
      <span>Event Lighting</span>
      <span>LED Robot</span>
    </div>
  </section>

</body>
</html>
```